Coach needs thank you cards (business card format) to deliver to customers. Model behavior

I am a coach who needs thank-you cards for customers and people to appreciate "exemplary behavior". First and foremost it is about the mindfulness of the people who have a great behavior to estimate and reward. The colors should contain silver and light like the logo of Mentorbrightpath.
Updates

The following should include the cards front and back. Front: Praise for: there should be room below to enter the name of the person. The fangs should be silver and light blue as on the logo which I have uploaded. Back: capitalized by date: exemplary behavior should be at the bottom right. mentorbrightpath.ch

```html
<!DOCTYPE html>
<html lang="de">
<head>
<meta charset="utf-8">
<title>Mentorbrightpath – Lobkarte</title>
<link rel="stylesheet" href="https://fonts.googleapis.com/css2?family=Questrial&display=swap">
<style>
  :root {
    --canvas: #ececec;
    --card-blue: #2c75bb;
    --ink-blue: #2f71ba;
    --paper: #ffffff;
    --white: #ffffff;
    --swash: #6d9fd4;
  }
  * { margin: 0; padding: 0; box-sizing: border-box; }
  html, body {
    width: 1200px; height: 1200px; overflow: hidden;
    background: var(--canvas);
    font-family: "Questrial", sans-serif;
  }
  .card {
    position: absolute;
    left: 281px;
    width: 638px;
    height: 364px;
    overflow: hidden;
  }
  .card--front { top: 209px; background: var(--card-blue); }
  .card--back { top: 634px; background: var(--paper); }

  .brand {
    position: absolute;
    left: 0; right: 0; top: 100px;
    display: flex; align-items: center; justify-content: center; gap: 10px;
    color: var(--white);
    font-size: 15px;
    line-height: 18px;
    letter-spacing: 3px;
    text-transform: uppercase;
  }
  .brand__dot {
    width: 13px; height: 13px;
    border: 1.5px solid var(--white);
    border-radius: 50%;
  }
  .front__title {
    position: absolute;
    left: 0; right: 0; top: 147px;
    text-align: center;
    color: var(--white);
    font-weight: 400;
    font-size: 22px;
    line-height: 28px;
    letter-spacing: 3px;
    word-spacing: 6px;
  }
  .front__swash {
    position: absolute;
    left: 209px; top: 238px;
    width: 221px; height: 6px;
    border-radius: 3px;
    background: linear-gradient(90deg, transparent, var(--swash) 20%, var(--swash) 80%, transparent);
    opacity: .7;
  }

  .back__line {
    position: absolute;
    left: 49px; top: 168px;
    height: 32px;
    display: flex; align-items: center;
    color: var(--ink-blue);
    white-space: nowrap;
  }
  .back__date {
    font-size: 24px;
    letter-spacing: 2px;
  }
  .back__divider {
    display: inline-block;
    width: 3px; height: 27px;
    background: var(--ink-blue);
    margin: 0 22px 0 28px;
  }
  .back__reason {
    font-size: 24px;
    letter-spacing: 1.5px;
    font-variant: small-caps;
  }
  .back__web {
    position: absolute;
    left: 0; right: 0; top: 336px;
    text-align: center;
    color: var(--ink-blue);
    font-size: 20px;
    line-height: 24px;
    letter-spacing: 1px;
    text-transform: uppercase;
  }
</style>
</head>
<body>
  <section class="card card--front">
    <div class="brand"><span class="brand__dot"></span><span class="brand__name">Mentorbrightpath</span></div>
    <h1 class="front__title">EIN LOB FÜR</h1>
    <div class="front__swash" role="img" aria-label="Dezentes geschwungenes Zierornament in Hellblau"></div>
  </section>

  <section class="card card--back">
    <p class="back__line"><span class="back__date">20.01.2018</span><span class="back__divider"></span><span class="back__reason">vorbildliches Verhalten</span></p>
    <p class="back__web">mentorbrightpath.ch</p>
  </section>
</body>
</html>
```